Empresa de tecnología busca diseño de tarjetas de presentación

Se requiere tarjeta de presentación impresa, con los datos de contacto y logo de la empresa. (se adjunta una imagen como referencia, esto no significa que deberá de ser igual)

```html
<!DOCTYPE html>
<html lang="es">
<head>
<meta charset="utf-8">
<title>Corvale Sistemas — Tarjetas de presentación</title>
<link href="https://fonts.googleapis.com/css2?family=Montserrat:wght@500;700&family=Open+Sans:wght@400;700&display=swap" rel="stylesheet">
<style>
  :root {
    --navy: #173a6e;
    --green: #6ab43a;
    --white: #ffffff;
    --backdrop: #e6e7e9;
    --band-ink: #0b1630;
  }
  * { box-sizing: border-box; margin: 0; padding: 0; }
  html, body { width: 1200px; height: 1200px; overflow: hidden; }
  body {
    background: var(--backdrop);
    font-family: "Open Sans", Arial, sans-serif;
    position: relative;
  }
  .card {
    position: absolute;
    top: 215px;
    width: 440px;
    height: 770px;
    overflow: hidden;
    box-shadow: 0 6px 18px rgba(0,0,0,.18);
  }
  .card--front { left: 120px; background: var(--white); }
  .card--back { left: 640px; background: var(--navy); }
  .card-shapes { position: absolute; inset: 0; width: 440px; height: 770px; }

  .brand {
    position: absolute;
    left: 0; right: 0;
    text-align: center;
    font-family: "Montserrat", Arial, sans-serif;
    font-weight: 700;
    font-size: 40px;
    letter-spacing: 0;
  }
  .card--front .brand { top: 165px; color: var(--navy); }
  .card--back .brand { top: 270px; color: var(--white); }

  .holder { position: absolute; left: 58px; top: 360px; color: var(--navy); }
  .holder-name {
    font-family: "Montserrat", Arial, sans-serif;
    font-weight: 700;
    font-size: 27px;
    letter-spacing: .5px;
  }
  .holder-role { color: var(--white); font-size: 17px; letter-spacing: .3px; margin-top: 2px; }

  .contact-list { position: absolute; left: 58px; list-style: none; color: var(--navy); font-size: 20px; }
  .contact-list li { display: flex; align-items: center; height: 31px; }
  .contact-list svg { width: 20px; height: 20px; margin-right: 22px; flex: none; }
  .contact-list--main { top: 430px; }
  .contact-list--support { top: 638px; }

  .ticket-band {
    position: absolute;
    left: 0; right: 0; top: 588px;
    height: 36px;
    background: var(--navy);
    color: var(--band-ink);
    font-weight: 700;
    font-size: 19px;
    line-height: 36px;
    padding-left: 58px;
  }
</style>
</head>
<body>

<section class="card card--front" aria-label="Frente de la tarjeta">
  <svg class="card-shapes" viewBox="0 0 440 770" aria-hidden="true">
    <polygon points="120,0 320,0 220,34" fill="var(--navy)"/>
    <polygon points="0,330 150,305 235,345 440,288 440,770 0,770" fill="var(--green)"/>
  </svg>

  <div class="brand">Corvale Sistemas</div>

  <div class="holder">
    <h1 class="holder-name">LUCÍA HERRERA</h1>
    <p class="holder-role">GERENTE MARKETING DIGITAL</p>
  </div>

  <ul class="contact-list contact-list--main">
    <li><svg viewBox="0 0 20 20"><path d="M5 2l3 4-2 2c1 2 3 4 5 5l2-2 4 3-2 3C9 17 3 11 2 5z" fill="var(--navy)"/></svg>(55)4100 2230 ext 214</li>
    <li><svg viewBox="0 0 20 20"><rect x="5" y="1" width="10" height="18" rx="2" fill="none" stroke="var(--navy)" stroke-width="2"/><circle cx="10" cy="15.5" r="1.2" fill="var(--navy)"/></svg>56 2207 0918</li>
    <li><svg viewBox="0 0 20 20"><rect x="2" y="5" width="16" height="11" fill="none" stroke="var(--navy)" stroke-width="1.6"/><path d="M2 5l8 6 8-6" fill="none" stroke="var(--navy)" stroke-width="1.6"/></svg>lucia.herrera@corvale.com</li>
    <li><svg viewBox="0 0 20 20"><path d="M10 1a6 6 0 0 0-6 6c0 5 6 12 6 12s6-7 6-12a6 6 0 0 0-6-6z" fill="var(--navy)"/><circle cx="10" cy="7" r="2.3" fill="var(--green)"/></svg>piso 12, Torre Alcea CDMX</li>
  </ul>

  <div class="ticket-band">Necesitas Levantar un ticket</div>

  <ul class="contact-list contact-list--support">
    <li><svg viewBox="0 0 20 20"><path d="M5 2l3 4-2 2c1 2 3 4 5 5l2-2 4 3-2 3C9 17 3 11 2 5z" fill="var(--navy)"/></svg>01 800 3100482</li>
    <li><svg viewBox="0 0 20 20"><rect x="2" y="5" width="16" height="11" fill="none" stroke="var(--navy)" stroke-width="1.6"/><path d="M2 5l8 6 8-6" fill="none" stroke="var(--navy)" stroke-width="1.6"/></svg>soporte@corvale.com</li>
  </ul>
</section>

<section class="card card--back" aria-label="Reverso de la tarjeta">
  <svg class="card-shapes" viewBox="0 0 440 770" aria-hidden="true">
    <polygon points="115,0 335,0 290,32 170,32" fill="var(--green)"/>
    <polygon points="0,478 225,510 440,455 440,770 0,770" fill="var(--green)"/>
  </svg>
  <div class="brand">Corvale Sistemas</div>
</section>

</body>
</html>
```